Landing page for a cyber security service provider called 'Lumen Grove'

The client is a new cyber security company in need of a website landing page at lumengrove.example.

Their visual identity is modern, playful, clean and uncluttered and represents innovation, connectivity and approachability.

The company logo is provided in black (attached) but the client is open to changing the colour to align with the new website design.

The landing page needs to contain:
- A call to action with a 'Get Started' button
-Links to blank 'How it works', 'Products', 'Pricing', 'About Us' and 'Contact Us' pages (that we'll fill out later)

Target Market(s)

Medium to large businesses who probably don't understand cyber / cyber security but need their business to be protected.

Industry/Entity Type

Cyber Security

Coding

Coded - Design and coding required

Number of Pages Required

1 page

Font styles to use
Sans Serif
Other font styles liked:
• Helvetica

Requirements
Nice to have
• Hero banner at the top of the landing page.
Should not have
• Should not look like a traditional cyber / cyber security design (eg no dark blue/ black, red/black colour combinations). Please no military styles (eg no shields, cannons, swords, guns)

```html
<!DOCTYPE html>
<html lang="en">
<head>
<meta charset="utf-8">
<title>Lumen Grove — Cyber Security for Modern Businesses</title>
<link rel="stylesheet" href="https://fonts.googleapis.com/css2?family=Lexend:wght@300;400;500&family=Poppins:wght@300;400;500;600&display=swap">
<style>
:root{
  --page:#f6f6f7;
  --ink:#2d2b30;
  --text:#222226;
  --muted:#6f6f76;
  --blue:#3a5be0;
  --blue-light:#6f8cf5;
  --yellow:#f1c21b;
  --white:#ffffff;
  --tab:#403e44;
  --tab-active:#36343a;
  --rule:#4a484e;
}
*{box-sizing:border-box;margin:0;padding:0}
html,body{width:1200px;height:5106px;overflow:hidden}
body{position:relative;background:var(--page);font-family:"Poppins",sans-serif;color:var(--text)}
a{color:inherit;text-decoration:none}
.abs{position:absolute}
.heading{font-family:"Lexend",sans-serif;font-weight:400;letter-spacing:.5px}
.mark{position:relative;display:inline-block}
.mark::after{content:"";position:absolute;left:-4px;right:-8px;bottom:-8px;height:12px;border-bottom:3px solid var(--yellow);border-radius:0 0 50% 50%}
.btn{position:absolute;display:flex;align-items:center;justify-content:center;background:var(--blue);color:var(--white);font-size:11px;font-weight:600;letter-spacing:.3px;border-radius:5px;text-transform:uppercase;box-shadow:0 4px 10px rgba(58,91,224,.25)}
.panel{position:absolute;left:14px;width:1172px}
.panel svg.shape{position:absolute;left:0;top:0;overflow:visible}
.panel svg.shape path{fill:var(--ink)}

/* nav */
.brand{left:90px;top:24px;display:flex;align-items:center;gap:12px;font-family:"Lexend",sans-serif;font-size:24px;font-weight:500;color:var(--text)}
.brand .dot{width:22px;height:22px;border-radius:50%;background:var(--text)}
.nav{left:556px;top:38px;display:flex;align-items:center;gap:34px;font-size:12px;text-transform:uppercase;color:var(--text)}
.nav svg{width:18px;height:18px}

/* hero */
.hero-title{left:90px;top:206px;font-size:60px;line-height:63px;color:var(--white)}
.hero-sub{left:90px;top:424px;font-size:13px;font-weight:500;color:var(--white)}
.hero-art{left:560px;top:110px;width:630px;height:640px;border-radius:46% 40% 40% 46%;background:radial-gradient(circle at 52% 50%,#f2c46e 0 7%,#7fdcf3 16%,#3fb4e2 34%,rgba(63,180,226,.35) 56%,rgba(45,43,48,0) 72%)}
.trust{top:666px;font-size:13px;color:var(--text)}
.counter{top:666px;font-size:12px;font-weight:600}
.counter span{color:#b6b6bd;font-weight:400}

/* about */
.about-art{left:0;top:763px;width:665px;height:427px;background:radial-gradient(ellipse at 62% 48%,#4fb8ea 0 10%,#8fd0f2 24%,#d6ecf8 44%,rgba(246,246,247,0) 68%)}
.about-title{left:720px;top:852px;font-size:40px}
.about-text{left:720px;top:936px;width:400px;font-size:15px;line-height:24px;color:var(--muted)}

/* how it works */
.center{left:0;width:1200px;text-align:center}
.section-title{font-size:40px}
.section-sub{font-size:13px;line-height:20px;color:var(--muted)}
.step{position:absolute;top:1412px;width:322px;height:115px;background:var(--white);border-radius:8px;box-shadow:0 6px 20px rgba(0,0,0,.06);padding:22px 20px 0 96px}
.step .icon{position:absolute;left:28px;top:24px;width:50px;height:50px;border-radius:10px;display:flex;align-items:center;justify-content:center}
.step .icon svg{width:24px;height:24px;fill:none;stroke:var(--white);stroke-width:2;stroke-linecap:round;stroke-linejoin:round}
.step h3{font-family:"Lexend",sans-serif;font-weight:400;font-size:21px;margin-bottom:8px}
.step p{font-size:12px;line-height:17px;color:var(--muted)}
.ic-green{background:linear-gradient(135deg,#2fc79a,#12906d)}
.ic-orange{background:linear-gradient(135deg,#ff9a62,#ea5a2e)}
.ic-blue{background:linear-gradient(135deg,#38b6ee,#1d8ad6)}

/* products */
.prod-title{left:85px;top:1724px;font-size:40px;color:var(--white)}
.prod-desc{left:90px;top:1802px;width:470px;font-size:12.5px;line-height:20px;color:var(--white)}
.prod-name{left:88px;top:1866px;font-size:27px;color:var(--white)}
.prod-sub{left:90px;top:1907px;font-size:13px;color:#d2d1d6}
.prod-rule{left:90px;top:1959px;width:460px;height:1px;background:var(--rule)}
.tab{position:absolute;top:2000px;height:42px;border-radius:6px;background:var(--tab);color:var(--white);font-size:12px;display:flex;align-items:center;justify-content:center}
.tab.active{background:var(--tab-active);border:2px solid var(--blue-light)}
.prod-art{left:635px;top:1701px;width:480px;height:393px;border-radius:10px;background:linear-gradient(135deg,#8ea6d8 0%,#b79fc0 40%,#efc2ad 70%,#c9a3a8 100%)}

/* pricing */
.plan{position:absolute;top:2487px;width:279px;height:442px;background:var(--white);border-radius:12px;box-shadow:0 8px 28px rgba(0,0,0,.06);text-align:center}
.plan .badge{display:inline-block;margin-top:22px;padding:6px 14px;background:#ececef;border-radius:5px;font-size:10px;font-weight:600}
.plan .price{margin-top:16px;font-weight:600;font-size:36px}
.plan .price small{font-size:13px;font-weight:500}
.plan .tag{margin-top:4px;font-size:12px;color:var(--muted)}
.plan ul{list-style:none;text-align:left;margin:30px 0 0 36px}
.plan li{display:flex;align-items:center;gap:10px;height:27px;font-size:12px;color:var(--muted)}
.plan li svg{width:12px;height:12px;stroke:var(--text);stroke-width:2.6;fill:none}
.plan .btn{left:74px;top:368px;width:131px;height:42px}

/* contact */
.contact-art{left:60px;top:3083px;width:535px;height:490px;border-radius:48% 44% 44% 48%;background:radial-gradient(circle at 55% 45%,#f1f5f8 0 8%,#9fd6f0 20%,#4fb3e4 36%,rgba(79,179,228,.3) 56%,rgba(45,43,48,0) 72%)}
.contact-title{left:726px;top:3122px;font-size:40px;color:var(--white)}
.contact-sub{left:732px;top:3184px;width:390px;font-size:12.5px;line-height:20px;color:#dedde2}
.label{position:absolute;font-size:10px;font-weight:600;color:var(--white);text-transform:uppercase}
.field{position:absolute;background:var(--white);border-radius:3px;font-size:12px;color:#9c9ca3;padding:11px 16px}

/* faq */
.faq-item{position:absolute;left:268px;width:664px;background:var(--white);border-radius:6px;box-shadow:0 4px 14px rgba(0,0,0,.04);padding:0 28px}
.faq-item h4{display:flex;justify-content:space-between;align-items:center;font-weight:400;font-size:14px;height:56px}
.faq-item h4 svg{width:10px;height:10px;fill:var(--text)}
.faq-item p{font-size:12.5px;line-height:20px;color:var(--muted);margin-top:2px}

/* cta + footer */
.cta{left:44px;top:4487px;width:1112px;height:158px;border-radius:16px;overflow:hidden;background:linear-gradient(100deg,#3552d6,#4666e6)}
.cta .glow{position:absolute;left:736px;top:-40px;width:520px;height:240px;border-radius:120px 0 0 120px;background:#5a77ee}
.cta h2{position:absolute;left:51px;top:26px;font-size:38px;color:var(--white)}
.cta p{position:absolute;left:51px;top:96px;width:600px;font-size:13px;line-height:20px;color:#e3e7ff}
.cta .go{position:absolute;left:834px;top:64px;display:flex;align-items:center;gap:16px;color:var(--white);font-size:17px;font-weight:500}
.f-brand{left:90px;top:4768px;width:220px;display:flex;flex-direction:column;align-items:flex-start;gap:16px;font-family:"Lexend",sans-serif;font-size:28px;font-weight:500;color:var(--white);white-space:nowrap}
.f-brand .dot{width:34px;height:34px;border-radius:50%;background:var(--white)}
.f-head{font-family:"Lexend",sans-serif;font-size:17px;color:var(--white)}
.f-links{list-style:none;font-size:12px;color:#d6d5da;line-height:22px}
.f-contact{font-size:12px;color:#d6d5da}
.f-contact div{display:flex;gap:12px;align-items:flex-start}
.f-contact svg{width:13px;height:13px;fill:var(--white);flex:none;margin-top:2px}
.news-input{left:859px;top:4819px;width:251px;height:46px;background:var(--white);border-radius:4px;font-size:11px;color:#9c9ca3;padding:15px 22px}
.news-btn{left:1061px;top:4819px;width:49px;height:46px;background:var(--blue);border-radius:0 4px 4px 0;display:flex;align-items:center;justify-content:center}
.social{position:absolute;top:4888px;width:28px;height:28px;border-radius:50%;background:var(--white)}
.legal{top:5046px;font-size:12px}
</style>
</head>
<body>

<!-- header -->
<div class="abs brand"><span class="dot"></span>Lumen Grove</div>
<nav class="abs nav">
  <svg viewBox="0 0 24 24"><path d="M3 11 12 3l9 8v10h-6v-6H9v6H3z" fill="#3a5be0"/></svg>
  <a href="#how">How it works</a><a href="#products">Products</a><a href="#pricing">Pricing</a><a href="#about">About us</a><a href="#contact">Contact us</a>
</nav>

<!-- hero -->
<section class="panel" style="top:91px;height:639px">
  <svg class="shape" width="1172" height="639"><path d="M0,24 Q0,0 24,0 H1148 Q1172,0 1172,24 V615 Q1172,639 1148,639 H690 C628,639 637,539 575,539 H24 Q0,539 0,515 Z"/></svg>
</section>
<div class="abs hero-art" role="img" aria-label="Glowing padlock on a circuit-board emblem"></div>
<h1 class="abs heading hero-title">Secure Your<br>Business with<br><span class="mark">Lumen Grove</span></h1>
<p class="abs hero-sub">Innovative Cyber Security Solutions For Modern Businesses</p>
<a class="btn" href="#pricing" style="left:88px;top:472px;width:156px;height:51px">Get Started</a>
<p class="abs trust" style="left:90px">More than 100+ companies trusted us</p>
<p class="abs counter" style="left:520px">01 / <span>03</span></p>

<!-- about -->
<div class="abs about-art" id="about" role="img" aria-label="Digital lock surrounded by flowing data particles"></div>
<h2 class="abs heading about-title">About <span class="mark">Lumen Grove</span></h2>
<p class="abs about-text">Lumen Grove is dedicated to providing innovative cyber security solutions for medium to large businesses. Our mission is to make cyber security accessible and effective, ensuring your business stays protected against modern threats.</p>
<a class="btn" href="#about" style="left:720px;top:1083px;width:140px;height:45px">Learn More</a>

<!-- how it works -->
<h2 class="abs center heading section-title" id="how" style="top:1246px">How It <span class="mark">Works</span></h2>
<p class="abs center section-sub" style="top:1333px">Explore our flexible pricing plans designed to meet the unique needs<br>of your business. Contact us for a custom quote.</p>
<div class="step" style="left:88px">
  <div class="icon ic-green"><svg viewBox="0 0 24 24"><path d="M6 3h8l4 4v14H6z"/><path d="M9 12h6M9 16h6"/></svg></div>
  <h3>Assess</h3><p>We evaluate your cyber security posture to identify vulnerabilities.</p>
</div>
<div class="step" style="left:438px">
  <div class="icon ic-orange"><svg viewBox="0 0 24 24"><circle cx="12" cy="12" r="8"/><path d="m8.5 12 2.5 2.5 4.5-5"/></svg></div>
  <h3>Protect</h3><p>Implement tailored solutions to safeguard your business.</p>
</div>
<div class="step" style="left:787px">
  <div class="icon ic-blue"><svg viewBox="0 0 24 24"><path d="M2 12s4-7 10-7 10 7 10 7-4 7-10 7S2 12 2 12z"/><circle cx="12" cy="12" r="3"/></svg></div>
  <h3>Monitor</h3><p>Continuous monitoring &amp; support to ensure ongoing protection.</p>
</div>

<!-- products -->
<section class="panel" id="products" style="top:1624px;height:637px">
  <svg class="shape" width="1172" height="637"><path d="M0,24 Q0,0 24,0 H1148 Q1172,0 1172,24 V613 Q1172,637 1148,637 H690 C628,637 637,534 575,534 H24 Q0,534 0,510 Z"/></svg>
</section>
<h2 class="abs heading prod-title">Lumen Grove <span class="mark">Products</span></h2>
<p class="abs prod-desc">A patch is data that is intended to be used to modify an existing software resource such as a program or a file</p>
<h3 class="abs heading prod-name">GroveNet</h3>
<p class="abs prod-sub">Advanced network security solutions.</p>
<div class="abs prod-rule"></div>
<div class="tab" style="left:90px;width:132px">GroveGuard</div>
<div class="tab active" style="left:236px;width:136px">GroveNet</div>
<div class="tab" style="left:385px;width:135px">GroveSecure</div>
<div class="abs prod-art" role="img" aria-label="Hands typing on a laptop keyboard with code overlay"></div>
<p class="abs trust" style="left:90px;top:2200px">Lumen Grove is dedicated to providing</p>
<p class="abs counter" style="left:520px;top:2200px">01 / <span>03</span></p>

<!-- pricing -->
<h2 class="abs center heading section-title" id="pricing" style="top:2323px">Our Pricing <span class="mark">Plan</span></h2>
<p class="abs center section-sub" style="top:2408px">Explore our flexible pricing plans designed to meet the unique needs<br>of your business. Contact us for a custom quote.</p>

<div class="plan" style="left:168px">
  <span class="badge">BASIC</span>
  <div class="price">$0<small>/Month</small></div>
  <p class="tag">Keep home and family on track</p>
  <ul>
    <li><svg viewBox="0 0 12 12"><path d="m1.5 6.5 3 3 6-7"/></svg>All unique templates</li>
    <li><svg viewBox="0 0 12 12"><path d="m1.5 6.5 3 3 6-7"/></svg>Mailings</li>
    <li><svg viewBox="0 0 12 12"><path d="m1.5 6.5 3 3 6-7"/></svg>Access to updates</li>
    <li><svg viewBox="0 0 12 12"><path d="m1.5 6.5 3 3 6-7"/></svg>Live chat support</li>
    <li><svg viewBox="0 0 12 12"><path d="m1.5 6.5 3 3 6-7"/></svg>Unlimited</li>
    <li><svg viewBox="0 0 12 12"><path d="m1.5 6.5 3 3 6-7"/></svg>Placing Orders</li>
  </ul>
  <a class="btn" href="#contact">Get Started</a>
</div>
<div class="plan" style="left:464px">
  <span class="badge">PREMIUM</span>
  <div class="price">14.99<small>/Month</small></div>
  <p class="tag">Keep home and family on track</p>
  <ul>
    <li><svg viewBox="0 0 12 12"><path d="m1.5 6.5 3 3 6-7"/></svg>All unique templates</li>
    <li><svg viewBox="0 0 12 12"><path d="m1.5 6.5 3 3 6-7"/></svg>Mailings</li>
    <li><svg viewBox="0 0 12 12"><path d="m1.5 6.5 3 3 6-7"/></svg>Access to updates</li>
    <li><svg viewBox="0 0 12 12"><path d="m1.5 6.5 3 3 6-7"/></svg>Live chat support</li>
    <li><svg viewBox="0 0 12 12"><path d="m1.5 6.5 3 3 6-7"/></svg>Unlimited</li>
    <li><svg viewBox="0 0 12 12"><path d="m1.5 6.5 3 3 6-7"/></svg>Placing Orders</li>
  </ul>
  <a class="btn" href="#contact">Get Started</a>
</div>
<div class="plan" style="left:763px">
  <span class="badge">ENTERPRISE</span>
  <div class="price">$17.99<small>/Month</small></div>
  <p class="tag">Keep home and family on track</p>
  <ul>
    <li><svg viewBox="0 0 12 12"><path d="m1.5 6.5 3 3 6-7"/></svg>All unique templates</li>
    <li><svg viewBox="0 0 12 12"><path d="m1.5 6.5 3 3 6-7"/></svg>Mailings</li>
    <li><svg viewBox="0 0 12 12"><path d="m1.5 6.5 3 3 6-7"/></svg>Access to updates</li>
    <li><svg viewBox="0 0 12 12"><path d="m1.5 6.5 3 3 6-7"/></svg>Live chat support</li>
    <li><svg viewBox="0 0 12 12"><path d="m1.5 6.5 3 3 6-7"/></svg>Unlimited</li>
    <li><svg viewBox="0 0 12 12"><path d="m1.5 6.5 3 3 6-7"/></svg>Placing Orders</li>
  </ul>
  <a class="btn" href="#contact">Get Started</a>
</div>

<!-- contact -->
<section class="panel" id="contact" style="top:3042px;height:641px">
  <svg class="shape" width="1172" height="641"><path d="M0,24 Q0,0 24,0 H1148 Q1172,0 1172,24 V617 Q1172,641 1148,641 H680 C622,641 652,537 592,537 H24 Q0,537 0,513 Z"/></svg>
</section>
<div class="abs contact-art" role="img" aria-label="Keyhole emblem wrapped in glowing digital panels"></div>
<h2 class="abs heading contact-title">Get In <span class="mark">Touch</span></h2>
<p class="abs contact-sub">Have questions or need more information? Fill out the form below, and our team will get back to you shortly</p>
<span class="label" style="left:732px;top:3256px">First Name</span>
<span class="label" style="left:924px;top:3256px">Last Name</span>
<div class="field" style="left:732px;top:3274px;width:184px;height:41px">Enter your name</div>
<div class="field" style="left:924px;top:3274px;width:188px;height:41px">Enter your name</div>
<span class="label" style="left:732px;top:3327px">Email Address</span>
<div class="field" style="left:732px;top:3347px;width:380px;height:40px">Enter email address</div>
<span class="label" style="left:732px;top:3401px">Message</span>
<div class="field" style="left:732px;top:3419px;width:380px;height:111px">Type your message</div>
<a class="btn" href="#contact" style="left:858px;top:3563px;width:128px;height:40px;font-size:13px">Submit</a>

<!-- faq -->
<h2 class="abs center heading section-title" style="top:3772px">Got Questions? We've Got <span class="mark">Answers!</span></h2>
<div class="faq-item" style="top:3867px;height:139px">
  <h4>What is cybersecurity?<svg viewBox="0 0 10 10"><path d="M1 3h8L5 8z"/></svg></h4>
  <p>Cybersecurity refers to the practice of protecting systems, networks, and programs from digital attacks. These attacks are usually aimed at accessing, changing, or destroying sensitive information, extorting money.</p>
</div>
<div class="faq-item" style="top:4029px"><h4>Why is cybersecurity important?<svg viewBox="0 0 10 10"><path d="M1 3h8L5 8z"/></svg></h4></div>
<div class="faq-item" style="top:4101px"><h4>What are common types of cyber threats?<svg viewBox="0 0 10 10"><path d="M1 3h8L5 8z"/></svg></h4></div>
<div class="faq-item" style="top:4173px"><h4>How can I protect myself from cyber threats?<svg viewBox="0 0 10 10"><path d="M1 3h8L5 8z"/></svg></h4></div>
<div class="faq-item" style="top:4245px"><h4>What should I do if I suspect a cyber attack?<svg viewBox="0 0 10 10"><path d="M1 3h8L5 8z"/></svg></h4></div>
<a class="btn" href="#faq" style="left:526px;top:4337px;width:148px;height:40px">See More FAQ's</a>

<!-- footer -->
<footer class="panel" style="top:4454px;height:652px">
  <svg class="shape" width="1172" height="652"><path d="M0,24 Q0,0 24,0 H1148 Q1172,0 1172,24 V652 H690 C628,652 637,575 575,575 H24 Q0,575 0,551 Z"/></svg>
</footer>
<div class="abs cta">
  <div class="glow"></div>
  <h2 class="heading"><span class="mark">Get Started Today</span></h2>
  <p>Ready to take control of your life? Sign up now and start using DayKeeper to organize, manage, and optimize every aspect of your life.</p>
  <a class="go" href="#contact">Contact Us Now
    <svg width="40" height="14" viewBox="0 0 40 14"><path d="M0 7h37M31 1l6 6-6 6" stroke="#fff" stroke-width="2" fill="none"/></svg></a>
</div>

<div class="abs f-brand"><span class="dot"></span>Lumen Grove</div>

<h4 class="abs f-head" style="left:347px;top:4730px">Quick Links</h4>
<ul class="abs f-links" style="left:347px;top:4762px">
  <li><a href="#how">How it works</a></li><li><a href="#products">Products</a></li><li><a href="#pricing">Pricing</a></li><li><a href="#about">About Us</a></li><li><a href="#contact">Contact Us</a></li>
</ul>

<h4 class="abs f-head" style="left:591px;top:4730px">Contact Us</h4>
<div class="abs f-contact" style="left:591px;top:4771px;width:220px">
  <div style="margin-bottom:22px"><svg viewBox="0 0 24 24"><path d="M6.6 10.8a15 15 0 0 0 6.6 6.6l2.2-2.2c.3-.3.7-.4 1-.2 1.1.4 2.3.6 3.6.6.6 0 1 .4 1 1V20c0 .6-.4 1-1 1A17 17 0 0 1 3 4c0-.6.4-1 1-1h3.5c.6 0 1 .4 1 1 0 1.3.2 2.5.6 3.6.1.3 0 .7-.2 1z"/></svg>+1 (555) 014-2290</div>
  <div style="margin-bottom:20px"><svg viewBox="0 0 24 24"><path d="M2 5h20v14H2zm2 2v.5l8 5 8-5V7z"/></svg><a href="mailto:info@lumengrove.example" style="text-decoration:underline">info@lumengrove.example</a></div>
  <div style="line-height:17px"><svg viewBox="0 0 24 24"><path d="M12 2a7 7 0 0 0-7 7c0 5 7 13 7 13s7-8 7-13a7 7 0 0 0-7-7zm0 9.5A2.5 2.5 0 1 1 12 6.5a2.5 2.5 0 0 1 0 5z"/></svg>Some address line goes<br>here city name</div>
</div>

<h4 class="abs f-head" style="left:859px;top:4730px">Newsletter</h4>
<p class="abs f-contact" style="left:859px;top:4767px;width:230px;line-height:17px">Subscribe newsletter for the latest offers and news</p>
<div class="abs news-input">Enter Email...</div>
<div class="abs news-btn"><svg width="18" height="12" viewBox="0 0 18 12"><path d="M0 6h16M11 1l5 5-5 5" stroke="#fff" stroke-width="1.8" fill="none"/></svg></div>
<span class="social" style="left:869px"></span>
<span class="social" style="left:904px"></span>
<span class="social" style="left:940px"></span>
<span class="social" style="left:976px"></span>

<p class="abs legal" style="left:90px;color:var(--text)">© Copyright 2024 Lumen Grove, All Rights Reserved</p>
<p class="abs legal" style="left:903px;color:var(--white)">Privacy Policy &nbsp; | &nbsp; Terms of Service</p>

</body>
</html>
```